Veltaro Resident Safety and Security

Need a website for our company. Please see attached outlines and files
Main Page
Veltaro
Design – Install – Maintain
Supporting the Safety and Security needs of your Community
Best in Class Systems for the Safety and Security of your Residents and Staff
Your Trusted Advisor
Solutions
Systems tailored to the needs of your facility
Skilled Nursing Facilities
Long Term Care
CCRC’s
Assisted Living
Independent Living
Access Control
Maglocks
Keypads
Prox readers (key fob, card, etc.)
Wireless locks
Multi-Tennant
Perimeter doors
Resident Apartment doors
Nurse Call
Tone / Visual
Fixed Stations
Dome Lights
T/V+ Audio
Fixed Stations
Dome Lights
Audio communication
Wireless
Fixed Stations
Resident Pendants
Hybrid Systems
Wired and Wireless integrated for seamless notification and reporting.
CCTV
Surveillance systems to fit your security needs and your budget
Remote Access, Local or Cloud Storage
Good, Better, Best proposals
Wander management
Door Alarming
Detection of wandering resident
Remote alarming and alerts
Delay elopement to allow for redirection
Network Infrastructure
Modern infrastructure for modern systems
Conference and Telepresence
Professionally installed systems to allow for seamless clear communications between teams across infinite distances.
Our Team
Mark Dunleavy – President
Paula Hobart – Vice President of Customer Success
Colin Marsh – Account Executive
Industry Associations
Granite Harbor Guild
Massachusetts chapter of the National Guild of Care Facility Stewards
Contact Us
Phone (603) 555-0172
Email Info@Veltaro-example.com
Facilities we serve
Independent Senior Living
Assisted Living
Memory Care
CCRC (Continuing Care Retirement Community)
Skilled Nursing / Rehab
Multi-Tenant
Outpatient Surgical Centers
Endoscopy Clinics
Acute Care
Urgent Care
Commercial Properties of all types
General notes
Imagery should invoke high tech, safety, security and include healthcare themes. the circuit board shield is our logo and a ghosted image as back ground or some animation that brings in the logo or the circuit board should be incorporated.
Veltaro is a systems integration company specializing in low voltage solutions for healthcare facilities and senior living communities. The company aims to leverage its industry expertise, and innovative products to become the market leader in systems integration, focusing on enhancing safety and operational efficiency.
Vision and Mission: Veltaro’s vision is to revolutionize integrated systems within healthcare and commercial environments by delivering innovative, reliable, and tailored solutions that enhance operational efficiency and patient care. The company is committed to setting new standards for resident safety and customer satisfaction.
Company Summary: Founded by experienced industry professionals, Veltaro specializes in the design, installation, and maintenance of systems including Access Control, Nurse Call, Delayed Egress, network infrastructure, and overhead paging primarily for healthcare clients.
Products and Services: The company offers a comprehensive range of low voltage systems including Nurse Call (wired and wireless), Wander Management, Access Control, and wired/wireless network infrastructure tailored for senior living and healthcare facilities.
Mission Statement
Veltaro was founded to fill a specific need. Senor living communities and healthcare facilities of all kinds face unique challenges in regards to technology and systems integration. Veltaro is perfectly positioned with an experienced management team, skilled technicians, industry relationships with suppliers and facility management groups. We have built our reputation on excellent customer service and the highest standards of integrity. Veltaro’s vision is to revolutionize integrated systems within healthcare and commercial environments by delivering innovative, reliable, and tailored solutions that enhance operational efficiency and patient care. We are committed to setting new standards for resident safety and customer satisfaction in every project we undertake.

Target Market(s)

Senior living communities staff and management

Industry/Entity Type

Systems Intergration

Coding

Coded - Design and coding required

Font styles to use
Serif
Sans Serif

Colors
0054AA
0677BA
7BADD7
CADEEF
E8F1F8
0094D4
00A9DD
6FCCEA
C7EBF8
E9F6FB

Requirements
Must have
• unique eye catching design including circuit board (PCB) type design and our supplied logo files

```html
<!DOCTYPE html>
<html lang="en">
<head>
<meta charset="UTF-8">
<title>Veltaro – Smart Systems for Safer Communities</title>
<link href="https://fonts.googleapis.com/css2?family=Poppins:ital,wght@0,400;0,500;0,600;0,700;1,400&display=swap" rel="stylesheet">
<style>
:root{
  --blue-deep:#0054AA;
  --blue:#0677BA;
  --sky:#0094D4;
  --cyan:#00A9DD;
  --ice:#E8F1F8;
  --mist:#CADEEF;
  --pale:#E9F6FB;
  --navy:#131a33;
  --ink:#1c2230;
  --muted:#6b7280;
  --line:#e7ebf0;
  --white:#ffffff;
}
*{box-sizing:border-box;margin:0;padding:0}
html,body{width:1200px;height:4274px;overflow:hidden}
body{position:relative;font-family:"Poppins",sans-serif;color:var(--ink);background:var(--white)}
.abs{position:absolute}

/* Hero */
.hero{position:absolute;left:0;top:0;width:1200px;height:640px;overflow:hidden}
.hero-photo{position:absolute;inset:0;background:linear-gradient(100deg,#3a3f45 0%,#6b5a48 30%,#8a6c52 55%,#5d4a3c 80%,#3a3430 100%)}
.hero-shade{position:absolute;inset:0;background:linear-gradient(180deg,rgba(10,20,40,.45),rgba(10,20,40,.55))}
.hero-curve{position:absolute;left:0;top:0}
.nav-logo{position:absolute;left:50px;top:30px;display:flex;align-items:center;gap:8px;color:var(--white);font-weight:600;font-size:16px}
.nav-logo .mark{width:26px;height:26px;border-radius:50%;background:var(--sky)}
.nav-links{position:absolute;left:435px;top:38px;display:flex;gap:30px;font-size:13px;color:var(--white);font-weight:500}
.btn{display:flex;align-items:center;justify-content:center;border-radius:30px;font-weight:600}
.nav-cta{position:absolute;left:1031px;top:33px;width:123px;height:30px;background:var(--white);color:var(--blue-deep);font-size:12px}
.hero-title{position:absolute;left:0;width:1200px;top:176px;text-align:center;color:var(--white);font-weight:700;font-size:58px;line-height:58px;letter-spacing:-.5px}
.hero-sub{position:absolute;left:0;width:1200px;top:318px;text-align:center;color:#f1f3f6;font-size:19px;line-height:26px}
.hero-cta{position:absolute;left:478px;top:402px;width:242px;height:46px;background:var(--white);color:var(--blue-deep);font-size:16px}

/* Feature cards */
.feature{position:absolute;top:545px;height:227px;background:var(--white);border-radius:10px;box-shadow:0 10px 30px rgba(20,40,80,.12);text-align:center;padding:0 28px}
.feature .icon{width:58px;height:58px;border-radius:50%;background:var(--ice);margin:33px auto 0;display:flex;align-items:center;justify-content:center}
.feature h3{font-size:19px;font-weight:600;margin-top:26px}
.feature p{font-size:13.5px;line-height:19px;color:var(--muted);margin-top:10px}
.feature.is-active{top:540px;height:237px;background:linear-gradient(160deg,var(--blue) 0%,var(--sky) 100%);color:var(--white);box-shadow:0 14px 34px rgba(0,84,170,.3)}
.feature.is-active .icon{background:rgba(255,255,255,.2)}
.feature.is-active p{color:#e6f1fb}

/* About */
.about-bg{position:absolute;left:0;top:847px;width:1200px;height:550px;background:linear-gradient(135deg,var(--ice) 0%,rgba(232,241,248,0) 45%)}
.about-blob{position:absolute;left:20px;top:921px;width:578px;height:382px;background:var(--mist);border-radius:62% 38% 44% 56% / 46% 52% 48% 54%}
.about-photo{position:absolute;left:42px;top:945px;width:534px;height:338px;background:linear-gradient(135deg,#c9b79d 0%,#e3d6c2 40%,#a7b4c0 75%,#8c96a3 100%);border-radius:62% 38% 44% 56% / 46% 52% 48% 54%}
.status-badge{position:absolute;left:427px;top:1188px;width:157px;height:65px;background:var(--white);border-radius:8px;box-shadow:0 8px 20px rgba(0,0,0,.12);display:flex;align-items:center;gap:12px;padding-left:14px}
.status-badge .tick{width:28px;height:28px;border-radius:50%;background:#e5f6ea;display:flex;align-items:center;justify-content:center}
.status-badge small{display:block;font-size:9px;color:var(--muted);font-weight:600;letter-spacing:.3px}
.status-badge strong{font-size:12px}
.eyebrow{position:absolute;left:629px;top:907px;font-size:13px;font-weight:600;color:var(--blue);letter-spacing:.3px}
.about-title{position:absolute;left:629px;top:932px;font-size:45px;line-height:45px;font-weight:700;color:var(--blue-deep)}
.about-copy{position:absolute;left:629px;top:1093px;width:510px;font-size:15.5px;line-height:25px;color:#3b4250}
.about-copy p+p{margin-top:20px}
.btn-primary{position:absolute;background:var(--blue-deep);color:var(--white)}
.about-cta{left:629px;top:1308px;width:143px;height:42px;font-size:15px}

/* Solutions */
.section-title{position:absolute;left:0;width:1200px;text-align:center;font-weight:600;font-size:30px}
.section-sub{position:absolute;left:0;width:1200px;text-align:center;font-size:15px;color:var(--muted)}
.solution{position:absolute;top:1598px;width:269px;height:253px;border:1px solid var(--line);border-radius:8px;text-align:center;padding:0 22px}
.solution .icon{width:60px;height:60px;border-radius:8px;margin:25px auto 0;display:flex;align-items:center;justify-content:center}
.solution h3{font-size:17px;font-weight:600;margin-top:28px}
.solution p{font-size:13px;line-height:21px;color:var(--muted);margin-top:12px}

/* Facilities */
.facilities-band{position:absolute;left:0;top:1926px}
.facilities-title{position:absolute;left:15px;top:2086px;font-size:35px;font-weight:700;color:var(--white)}
.facilities-copy{position:absolute;left:15px;top:2152px;width:560px;font-size:16px;line-height:26px;color:#eaf5fd}
.pill{position:absolute;width:272px;height:43px;background:rgba(255,255,255,.14);border-radius:5px;display:flex;align-items:center;gap:10px;padding-left:12px;font-size:15px;color:var(--white)}
.pill .dot{width:16px;height:16px;border-radius:50%;background:var(--white);display:flex;align-items:center;justify-content:center}
.facilities-cta{position:absolute;left:15px;top:2430px;width:201px;height:43px;background:var(--white);color:var(--blue-deep);font-size:15px}
.dashboard{position:absolute;left:622px;top:2112px;width:563px;height:340px;background:var(--white);border-radius:10px;box-shadow:0 18px 40px rgba(0,30,70,.3);transform:rotate(2deg);padding:20px 24px}
.dash-dots{display:flex;gap:8px}
.dash-dots span{width:10px;height:10px;border-radius:50%}
.dash-row{display:flex;gap:16px;margin-top:22px}
.dash-stat{flex:1;height:74px;border-radius:6px;padding:12px 16px}
.dash-stat small{display:block;font-size:11px;color:var(--muted)}
.dash-stat b{font-size:22px}
.dash-bar{height:32px;background:#eef1f4;border-radius:4px;margin-top:14px}
.dash-report{height:106px;background:#f1f3f5;border-radius:4px;margin-top:14px;display:flex;align-items:center;justify-content:center;gap:8px;font-size:13px;color:#9aa1ab}

/* Values */
.value{position:absolute;top:2719px;width:360px;text-align:center}
.value .hex{width:120px;height:120px;margin:0 auto;display:flex;align-items:center;justify-content:center;background:var(--ice);clip-path:polygon(50% 0,100% 25%,100% 75%,50% 100%,0 75%,0 25%)}
.value h3{font-size:19px;font-weight:600;margin-top:22px}
.value p{font-size:13px;line-height:19px;color:var(--muted);margin:6px auto 0;width:300px}

/* Leadership */
.leader-blob{position:absolute;left:95px;top:3079px;width:503px;height:598px;background:var(--ice);border-radius:48% 52% 44% 56% / 40% 46% 54% 60%}
.leader-photo{position:absolute;left:170px;top:3100px;width:365px;height:560px;background:linear-gradient(180deg,#b9c6d3 0%,#8e9aa8 45%,#3a4250 100%);border-radius:50% 50% 46% 54% / 38% 40% 60% 62%}
.stars{position:absolute;left:622px;top:3182px;display:flex;gap:2px}
.leader-quote{position:absolute;left:622px;top:3213px;width:470px;font-size:29px;line-height:34px;font-weight:600}
.leader-bio{position:absolute;left:622px;top:3360px;width:470px;font-size:15px;line-height:23px;font-style:italic;color:#555c68}
.leader-name{position:absolute;left:622px;top:3430px;font-size:17px;font-weight:600;color:var(--blue-deep)}
.leader-role{position:absolute;left:622px;top:3458px;font-size:12px;letter-spacing:1px;color:#8a909a}
.leader-rule{position:absolute;left:622px;top:3506px;width:460px;height:1px;background:var(--line)}
.team{position:absolute;top:3527px}
.team b{display:block;font-size:13px;font-weight:600}
.team span{display:block;font-size:11px;color:var(--muted)}

/* CTA & footer */
.footer-wave{position:absolute;left:0;top:3780px}
.cta{position:absolute;left:151px;top:3703px;width:906px;height:176px;border-radius:16px;background:linear-gradient(110deg,var(--blue-deep) 0%,var(--blue) 55%,var(--cyan) 100%);box-shadow:0 16px 40px rgba(0,84,170,.25)}
.cta h2{position:absolute;left:32px;top:44px;font-size:35px;font-weight:600;color:var(--white)}
.cta p{position:absolute;left:32px;top:88px;font-size:19px;color:#e3f0fb}
.cta-btn{position:absolute;left:679px;top:57px;width:186px;height:65px;background:var(--white);color:var(--blue-deep);font-size:22px}
.footer{position:absolute;left:0;top:3884px;width:1200px;height:390px;background:var(--navy);color:#c7ccd6}
.footer-logo{position:absolute;left:15px;top:130px;display:flex;align-items:center;gap:8px;color:var(--sky);font-size:16px;font-weight:600}
.footer-logo .mark{width:26px;height:26px;border-radius:50%;background:var(--sky)}
.footer-about{position:absolute;left:15px;top:206px;width:270px;font-size:12.5px;line-height:19px}
.socials{position:absolute;left:15px;top:272px;display:flex;gap:16px}
.socials span{width:26px;height:26px;border-radius:50%;background:#2a3250;display:flex;align-items:center;justify-content:center}
.footer-col{position:absolute;top:128px}
.footer-col h4{font-size:12.5px;font-weight:600;letter-spacing:1px;color:var(--white);margin-bottom:16px}
.footer-col li{list-style:none;font-size:12.5px;line-height:18px;margin-bottom:9px;display:flex;gap:10px;align-items:flex-start}
.footer-col .bullet{width:11px;height:11px;border-radius:50%;background:var(--sky);margin-top:4px;flex:none}
.copyright{position:absolute;left:0;top:374px;width:1200px;text-align:center;font-size:12.5px;color:#9aa1b0}
</style>
</head>
<body>

<!-- Hero -->
<section class="hero">
  <div class="hero-photo" role="img" aria-label="Photo of senior residents sharing a meal together in a bright dining room"></div>
  <div class="hero-shade"></div>
  <svg class="hero-curve" width="1200" height="640" viewBox="0 0 1200 640"><path d="M0 560 C 300 520, 650 500, 900 560 S 1150 620 1200 600 L1200 640 L0 640 Z" fill="#fff"/></svg>
  <div class="nav-logo"><span class="mark"></span>Veltaro</div>
  <nav class="nav-links"><span>Home</span><span>About</span><span>Services</span><span>Team</span></nav>
  <div class="btn nav-cta">Get a Quote</div>
  <h1 class="hero-title">Smart Systems for<br>Safer Communities</h1>
  <p class="hero-sub">The single source for design, installation, sales, and maintenance<br>of low-voltage systems for senior living and healthcare facilities.</p>
  <div class="btn hero-cta">Explore Our Solutions</div>
</section>

<article class="feature" style="left:60px;width:345px">
  <div class="icon"><svg width="24" height="24" viewBox="0 0 24 24" fill="none" stroke="#0054AA" stroke-width="2.4" stroke-linecap="round"><path d="M5 19 19 5M14 5h5v5M5 14v5h5"/></svg></div>
  <h3>Design &amp; Install</h3>
  <p>Comprehensive planning and installation for all low-voltage systems tailored to your facility.</p>
</article>
<article class="feature is-active" style="left:418px;width:362px">
  <div class="icon"><svg width="24" height="24" viewBox="0 0 24 24"><path d="M13 2 5 14h6l-1 8 8-12h-6z" fill="#fff"/></svg></div>
  <h3>Systems Integration</h3>
  <p>Nurse Call, Access Control, and Infrastructure working together for operational efficiency.</p>
</article>
<article class="feature" style="left:795px;width:345px">
  <div class="icon"><svg width="24" height="24" viewBox="0 0 24 24" fill="none" stroke="#0054AA" stroke-width="2.6" stroke-linecap="round"><path d="M5 5l14 14M19 5 5 19"/></svg></div>
  <h3>Service &amp; Sales</h3>
  <p>Your single source resource providing ongoing maintenance and product sales.</p>
</article>

<!-- About -->
<div class="about-bg"></div>
<div class="about-blob"></div>
<div class="about-photo" role="img" aria-label="Overhead photo of a team working at laptops on a shared desk"></div>
<div class="status-badge">
  <span class="tick"><svg width="14" height="14" viewBox="0 0 24 24" fill="none" stroke="#22a355" stroke-width="3" stroke-linecap="round"><path d="M5 12l5 5 9-10"/></svg></span>
  <div><small>SYSTEM STATUS</small><strong>Operational</strong></div>
</div>
<p class="eyebrow">ABOUT VELTARO</p>
<h2 class="about-title">Revolutionizing Safety<br>&amp;<br>Patient Care</h2>
<div class="about-copy">
  <p>Veltaro was founded to fill a specific need. Senior living communities and healthcare facilities face unique challenges regarding technology. We leverage industry expertise to enhance safety and operational efficiency.</p>
  <p>Our vision is to revolutionize integrated systems within healthcare environments by delivering innovative, reliable solutions tailored to your needs.</p>
</div>
<div class="btn btn-primary about-cta">Read More</div>

<!-- Solutions -->
<h2 class="section-title" style="top:1470px">Comprehensive Solutions</h2>
<p class="section-sub" style="top:1518px">Tailored low-voltage systems for modern healthcare.</p>

<article class="solution" style="left:15px">
  <div class="icon" style="background:#1f2430"><svg width="22" height="22" viewBox="0 0 24 24" fill="#fff"><circle cx="12" cy="8" r="4"/><path d="M4 21c0-5 4-7 8-7s8 2 8 7z"/></svg></div>
  <h3>Nurse Call Systems</h3>
  <p>Wired and wireless options allowing residents to call for help. Direct communication to caregivers reduces risk.</p>
</article>
<article class="solution" style="left:315px">
  <div class="icon" style="background:#f1e9fb"><svg width="24" height="24" viewBox="0 0 24 24" fill="none" stroke="#8b3fe0" stroke-width="2.2" stroke-linecap="round"><circle cx="9" cy="4" r="1.6" fill="#8b3fe0"/><path d="M9 8l-2 6 3 2-1 5M7 14l-3 3M9 9l3 3h3M15 12h6M19 10l2 2-2 2"/></svg></div>
  <h3>Wander Management</h3>
  <p>Secure transmitters lock doors to prevent eloping and sound alarms if a resident enters the reception field.</p>
</article>
<article class="solution" style="left:616px">
  <div class="icon" style="background:#e3eefb"><svg width="22" height="22" viewBox="0 0 24 24" fill="#1f6fd1"><rect x="3" y="6" width="18" height="15" rx="2"/><rect x="9" y="3" width="6" height="5" rx="1"/><circle cx="12" cy="12" r="2.2" fill="#e3eefb"/><path d="M8 18c0-2 2-3 4-3s4 1 4 3z" fill="#e3eefb"/></svg></div>
  <h3>Access Control</h3>
  <p>Control entry, log events, and generate incident reports. Essential security for facilities of all types.</p>
</article>
<article class="solution" style="left:915px">
  <div class="icon" style="background:#e2f6e9"><svg width="22" height="22" viewBox="0 0 24 24" fill="#1f9d55"><rect x="3" y="4" width="18" height="7" rx="1.5"/><rect x="3" y="13" width="18" height="7" rx="1.5"/><circle cx="16.5" cy="7.5" r="1" fill="#e2f6e9"/><circle cx="16.5" cy="16.5" r="1" fill="#e2f6e9"/></svg></div>
  <h3>Infrastructure</h3>
  <p>Network cable, switches, and wireless access points. Constant upgrades to keep your facility connected.</p>
</article>

<!-- Facilities -->
<svg class="facilities-band" width="1200" height="650" viewBox="0 0 1200 650">
  <defs><linearGradient id="bandFill" x1="0" y1="0" x2="1" y2="1"><stop offset="0" stop-color="#0677BA"/><stop offset="1" stop-color="#0094D4"/></linearGradient></defs>
  <path d="M0 91 L1200 0 L1200 547 L0 639 Z" fill="url(#bandFill)"/>
</svg>
<h2 class="facilities-title">Facilities We Serve</h2>
<p class="facilities-copy">We provide tailored solutions for a wide range of healthcare and commercial environments.</p>
<div class="pill" style="left:15px;top:2236px"><span class="dot"><svg width="10" height="10" viewBox="0 0 24 24" fill="none" stroke="#0677BA" stroke-width="4"><path d="M5 12l5 5 9-10"/></svg></span>Independent Senior Living</div>
<div class="pill" style="left:304px;top:2236px"><span class="dot"><svg width="10" height="10" viewBox="0 0 24 24" fill="none" stroke="#0677BA" stroke-width="4"><path d="M5 12l5 5 9-10"/></svg></span>Assisted Living</div>
<div class="pill" style="left:15px;top:2296px"><span class="dot"><svg width="10" height="10" viewBox="0 0 24 24" fill="none" stroke="#0677BA" stroke-width="4"><path d="M5 12l5 5 9-10"/></svg></span>Skilled Nursing / Rehab</div>
<div class="pill" style="left:304px;top:2296px"><span class="dot"><svg width="10" height="10" viewBox="0 0 24 24" fill="none" stroke="#0677BA" stroke-width="4"><path d="M5 12l5 5 9-10"/></svg></span>Memory Care</div>
<div class="pill" style="left:15px;top:2356px"><span class="dot"><svg width="10" height="10" viewBox="0 0 24 24" fill="none" stroke="#0677BA" stroke-width="4"><path d="M5 12l5 5 9-10"/></svg></span>Urgent Care &amp; Clinics</div>
<div class="pill" style="left:304px;top:2356px"><span class="dot"><svg width="10" height="10" viewBox="0 0 24 24" fill="none" stroke="#0677BA" stroke-width="4"><path d="M5 12l5 5 9-10"/></svg></span>Commercial Properties</div>
<div class="btn facilities-cta">View All Industries</div>

<div class="dashboard">
  <div class="dash-dots"><span style="background:#f26b5b"></span><span style="background:#f4bf3a"></span><span style="background:#3fc35c"></span></div>
  <div class="dash-row">
    <div class="dash-stat" style="background:#eef4fb"><small>ACTIVE CALLS</small><b style="color:#0054AA">3</b></div>
    <div class="dash-stat" style="background:#ebf8ef"><small>SYSTEM STATUS</small><b style="color:#1f9d55">Online</b></div>
  </div>
  <div class="dash-bar" style="width:62%"></div>
  <div class="dash-bar"></div>
  <div class="dash-report"><svg width="14" height="14" viewBox="0 0 24 24" fill="none" stroke="#9aa1ab" stroke-width="2"><path d="M3 3v18h18M7 15l4-4 3 3 5-6"/></svg>Real-Time Reporting</div>
</div>

<!-- Values -->
<h2 class="section-title" style="top:2634px">Driven by Values</h2>
<article class="value" style="left:59px">
  <div class="hex"><svg width="30" height="30" viewBox="0 0 24 24"><path d="M2 12s4-7 10-7 10 7 10 7-4 7-10 7S2 12 2 12z" fill="#0054AA"/><circle cx="12" cy="12" r="3.5" fill="#E8F1F8"/><circle cx="12" cy="12" r="1.8" fill="#0054AA"/></svg></div>
  <h3>Our Vision</h3>
  <p>Revolutionize integrated systems within healthcare by delivering innovative, reliable solutions.</p>
</article>
<article class="value" style="left:419px">
  <div class="hex"><svg width="26" height="26" viewBox="0 0 24 24" fill="#0054AA"><path d="M20 4c-5 0-9 3-11 8l3 3c5-2 8-6 8-11z"/><path d="M8 13l-4 1 3-4h3zM11 16l-1 4 4-3v-3zM6 16l-2 4 4-2z"/></svg></div>
  <h3>Our Mission</h3>
  <p>Setting new standards for resident safety and customer satisfaction in every project.</p>
</article>
<article class="value" style="left:779px">
  <div class="hex"><svg width="30" height="26" viewBox="0 0 28 24" fill="#0054AA"><rect x="1" y="7" width="4" height="10" rx="1"/><rect x="23" y="7" width="4" height="10" rx="1"/><path d="M6 8h5l3 2 3-2h5v9l-7 4-9-4z"/></svg></div>
  <h3>Integrity</h3>
  <p>Founded by industry experts to fill a specific need with the highest standards of integrity.</p>
</article>

<!-- Leadership -->
<div class="leader-blob"></div>
<div class="leader-photo" role="img" aria-label="Portrait of the company president in a suit"></div>
<div class="stars">
  <svg width="80" height="14" viewBox="0 0 80 14" fill="#f5b700"><path id="star" d="M7 0l2 4.6 5 .5-3.8 3.3 1.1 5L7 11 2.7 13.4l1.1-5L0 5.1l5-.5z"/><use href="#star" x="16"/><use href="#star" x="32"/><use href="#star" x="48"/><use href="#star" x="64"/></svg>
</div>
<blockquote class="leader-quote">"We have built our reputation on excellent customer service and the highest standards of integrity."</blockquote>
<p class="leader-bio">Mark brings 20 years of telecommunications experience and a proven record of building exceptional teams.</p>
<p class="leader-name">Mark Dunleavy</p>
<p class="leader-role">PRESIDENT, VELTARO</p>
<div class="leader-rule"></div>
<div class="team" style="left:622px"><b>Paula Hobart</b><span>VP Customer Success</span></div>
<div class="team" style="left:775px"><b>Colin Marsh</b><span>Account Executive</span></div>

<!-- CTA & Footer -->
<svg class="footer-wave" width="1200" height="110" viewBox="0 0 1200 110"><path d="M0 104 C 400 110, 800 80, 1000 40 S 1180 10 1200 5 L1200 110 L0 110 Z" fill="#131a33"/></svg>
<footer class="footer">
  <div class="footer-logo"><span class="mark"></span>Veltaro</div>
  <p class="footer-about">Specializing in low voltage solutions for healthcare facilities and senior living communities.</p>
  <div class="socials">
    <span><svg width="10" height="10" viewBox="0 0 10 10"><rect width="10" height="10" rx="2" fill="#c7ccd6"/></svg></span>
    <span><svg width="12" height="10" viewBox="0 0 24 18" fill="none" stroke="#c7ccd6" stroke-width="2.5"><rect x="1" y="1" width="22" height="16" rx="2"/><path d="M1 2l11 8 11-8"/></svg></span>
  </div>
  <div class="footer-col" style="left:315px">
    <h4>QUICK LINKS</h4>
    <ul><li>Home</li><li>About Us</li><li>Products &amp; Services</li><li>Contact</li></ul>
  </div>
  <div class="footer-col" style="left:614px">
    <h4>CONTACT INFO</h4>
    <ul>
      <li><svg width="13" height="13" viewBox="0 0 24 24" fill="#0094D4"><path d="M6 2l4 5-2 3c1 3 3 5 6 6l3-2 5 4-2 4C11 22 2 13 2 4z"/></svg>(603) 555-0172</li>
      <li><svg width="13" height="11" viewBox="0 0 24 18" fill="#0094D4"><rect width="24" height="18" rx="2"/><path d="M1 2l11 8 11-8" stroke="#131a33" stroke-width="2" fill="none"/></svg>Info@Veltaro-example.com</li>
      <li><svg width="11" height="14" viewBox="0 0 18 24" fill="#0094D4"><path d="M9 0a9 9 0 0 0-9 9c0 7 9 15 9 15s9-8 9-15a9 9 0 0 0-9-9z"/><circle cx="9" cy="9" r="3" fill="#131a33"/></svg>New England Area</li>
    </ul>
  </div>
  <div class="footer-col" style="left:915px;width:250px">
    <h4>ASSOCIATIONS</h4>
    <ul>
      <li><span class="bullet"></span>Granite Harbor Guild</li>
      <li><span class="bullet"></span>National Guild of Care Facility Stewards (MA)</li>
    </ul>
  </div>
  <p class="copyright">© 2024 Veltaro. All Rights Reserved.</p>
</footer>
<section class="cta">
  <h2>Ready to Transform Your Facility?</h2>
  <p>Contact us today to design your low-voltage solution.</p>
  <div class="btn cta-btn">Get a Qoute</div>
</section>

</body>
</html>
```